Real Estate Templates in Canva

I need someone to create a robust set of Canva template designs for my real estate company team, to streamline content. I need a catalog for my agents to easily go in and pick from different designs and customize for themselves. The correct candidate can emulate the style found on these sites., and in the attached images. I have also uploaded logos to be used.(https://www.brindlehomegroup.com/) and (https://meetkoravel.com/)

I want a fantastic sharp style that has great color blend and is attractive and matches my brand well.

The correct candidate will have access to my Canva Brand Kit and build templates inside of my account.

Also attached is a screenshot of my main color codes

The types of templates can include, but not be limited to the following:
BOTH DIGITAL FOR SOCIAL MEDIA AND PRINT VERSIONS
Listings flyers
Clients testimonials
market stats
open houses
Realtor Insights
Realtor analysis
sold properties
new listing properties
under contract properties
coming soon properties
Bullet points summarizing key data
Photo of the client at closing
Photo of the client at their home

Property Listing Template:

Description of the property
High-quality images
Key features and amenities
Open House Invitation:

Date, time, and location details
Compelling visuals of the property
Call-to-action for attendance
Just Sold Announcement:

Property details (address, price, etc.)
Celebratory message
Testimonials from satisfied clients
Testimonial Template:

Client testimonial
Photo of the client (with permission)
Brief background or story
Market Update Infographic:

Visual representation of current market trends
Realtor's insights and analysis
Buyer's Guide:

Step-by-step guide for homebuyers
Infographics explaining the buying process
Tips and advice for a successful purchase
Seller's Guide:

Information on preparing a home for sale
Infographics on the selling process
Tips for maximizing property value
Seasonal Greetings Template:

Personalized message for clients
Festive visuals or themes
Wishes for a successful year ahead
Neighborhood Highlight:

Showcase a specific neighborhood
Key attractions, schools, amenities
Testimonials from residents (if available)
Behind-the-Scenes:

Photos or videos of the realtor at work
Personalized messages about the real estate process
Humanizing content to connect with the audience
Infographic: Benefits of Working with a Realtor:

Visual representation of the advantages
Statistics or data supporting the benefits
Clear, concise points for easy consumption
Interactive Polls or Quizzes:

Engage the audience with fun polls
Real estate-related quizzes
Encourage interaction and sharing
Client Appreciation Post:

Thanking clients for their trust
Sharing success stories
Expressing gratitude with visuals
Video Tour Teaser:

Sneak peek of a property tour
Create excitement and anticipation

Target Market(s)

General Population ages 30-70

Requirements
Must have
• 60 plus designs
Nice to have
• 100 plus designs

```html
<!DOCTYPE html>
<html lang="en">
<head>
<meta charset="UTF-8">
<title>Brindle Home Group – Client Testimonial</title>
<link href="https://fonts.googleapis.com/css2?family=Roboto:wght@400;500&family=Yellowtail&display=swap" rel="stylesheet">
<style>
  :root {
    --brand-orange: #f39a2b;
    --star-gold: #f7b13c;
    --white: #ffffff;
    --backdrop-top: #a8abb0;
    --backdrop-bottom: #a2a59f;
    --portrait-blue: #5b80ab;
    --portrait-green: #6f8a58;
  }
  html, body {
    margin: 0;
    padding: 0;
    width: 776px;
    height: 1200px;
    overflow: hidden;
  }
  .testimonial-card {
    position: relative;
    width: 776px;
    height: 1200px;
    overflow: hidden;
    font-family: "Roboto", Arial, sans-serif;
  }
  .backdrop-photo {
    position: absolute;
    inset: 0;
    background: linear-gradient(180deg, var(--backdrop-top) 0%, var(--backdrop-bottom) 100%);
  }
  .brand {
    position: absolute;
    left: 41px;
    top: 40px;
    display: flex;
    align-items: center;
    gap: 12px;
  }
  .brand-dot {
    width: 75px;
    height: 75px;
    border-radius: 50%;
    background: var(--brand-orange);
  }
  .brand-name {
    color: var(--brand-orange);
    font-weight: 500;
    line-height: 1;
  }
  .brand-main {
    display: block;
    font-size: 34px;
    letter-spacing: 0.5px;
  }
  .brand-sub {
    display: block;
    font-size: 15px;
    letter-spacing: 5.5px;
    margin-top: 4px;
  }
  .quote-frame {
    position: absolute;
    left: 119px;
    top: 174px;
    width: 514px;
    height: 828px;
    border: 12px solid var(--white);
  }
  .quote-mark {
    position: absolute;
    left: 288px;
    top: 238px;
  }
  .rating {
    position: absolute;
    left: 275px;
    top: 435px;
  }
  .quote-text {
    position: absolute;
    left: 150px;
    width: 476px;
    top: 516px;
    margin: 0;
    text-align: center;
    color: var(--white);
    font-size: 27.5px;
    line-height: 39.7px;
    font-weight: 400;
  }
  .quote-author {
    position: absolute;
    left: 150px;
    width: 476px;
    top: 944px;
    margin: 0;
    text-align: center;
    color: var(--white);
    font-family: "Yellowtail", "Brush Script MT", cursive;
    font-size: 42px;
    line-height: 1.2;
  }
  .client-photo {
    position: absolute;
    left: 558px;
    top: 927px;
    width: 152px;
    height: 152px;
    border-radius: 50%;
    background: linear-gradient(160deg, var(--portrait-green) 0%, var(--portrait-blue) 100%);
  }
</style>
</head>
<body>
  <main class="testimonial-card">
    <div class="backdrop-photo" role="img" aria-label="Photo of a large modern home with lawn and front walkway, under a soft grey overlay"></div>

    <header class="brand">
      <div class="brand-dot" aria-hidden="true"></div>
      <div class="brand-name">
        <span class="brand-main">BRINDLE</span>
        <span class="brand-sub">HOME GROUP</span>
      </div>
    </header>

    <section class="quote-frame" aria-hidden="true"></section>

    <svg class="quote-mark" width="202" height="148" viewBox="0 0 202 148" aria-hidden="true">
      <path fill="#ffffff" d="M0,147 L0,70 C0,35 18,12 42,0 L50,10 C40,22 36,38 38,60 L86,60 L86,147 Z"/>
      <path fill="#ffffff" transform="translate(114,0)" d="M0,147 L0,70 C0,35 18,12 42,0 L50,10 C40,22 36,38 38,60 L86,60 L86,147 Z"/>
    </svg>

    <svg class="rating" width="226" height="34" viewBox="0 0 226 34" role="img" aria-label="Five star rating">
      <defs>
        <polygon id="star" points="17,0 21.2,11.6 33.6,12 23.8,19.6 27.3,31.5 17,24.5 6.7,31.5 10.2,19.6 0.4,12 12.8,11.6" fill="#f7b13c"/>
      </defs>
      <use href="#star" x="0"/>
      <use href="#star" x="48"/>
      <use href="#star" x="96"/>
      <use href="#star" x="144"/>
      <use href="#star" x="192"/>
    </svg>

    <p class="quote-text">Brindle Home Group's expertise<br>and guidance transformed my<br>dream of owning a home into<br>a tangible reality. Their<br>profound knowledge of the<br>industry ensured I received<br>the highest yield for my<br>estate, and the entire journey<br>felt nothing short of magical.</p>

    <p class="quote-author">-Owen Hartley</p>

    <div class="client-photo" role="img" aria-label="Portrait photo of the client outdoors"></div>
  </main>
</body>
</html>
```